I want to revise my business card design and get a more modern and up to date design.

Brolvane Handyman Sevices originated from a family-owned and operated contractor business, performing home renovation, addition, and construction work in the NYC area since 2004. Today, we specialize in reliable and affordable handyman services for residential and commercial clients In 2014, we expanded to northern New Jersey. In 2016, we brought quality home improvement and repair services to new Bucks County, PA, and nearby New Jersey areas.
Target Market(s)
Home owners and business that might be looking for a General contractor, handyman, cleaning services and Home maintenance and property.
Industry/Entity Type
Construction Company
Contact Information for Business Card
I am open to new ideas
Colors
Designer to choose colors to be used in the design.
Look and feel
Each slider illustrates characteristics of the customer's brand and the style your logo design should communicate.

```html
<!DOCTYPE html>
<html lang="en">
<head>
<meta charset="utf-8">
<title>Brolvane Handyman Sevices – Business Card</title>
<link rel="stylesheet" href="https://fonts.googleapis.com/css2?family=Maven+Pro:wght@400;500;600;700;800&display=swap">
<style>
  :root {
    --stage-red: #e82026;
    --card-red: #ed2329;
    --brand-red: #e8232a;
    --ink: #1f1f1f;
    --white: #ffffff;
    --gold: #ffd42a;
    --badge-grey: #d9d9d9;
  }
  * { margin: 0; padding: 0; box-sizing: border-box; }
  html, body { width: 1200px; height: 1000px; overflow: hidden; }
  body {
    position: relative;
    background: var(--stage-red);
    font-family: "Maven Pro", sans-serif;
  }
  .card {
    position: absolute;
    left: 256px;
    width: 689px;
    height: 394px;
  }
  .card--front { top: 86px; background: var(--card-red); }
  .card--back { top: 517px; background: var(--white); color: var(--ink); }

  /* Brand wordmark */
  .brand {
    position: absolute;
    display: flex;
    align-items: center;
    color: var(--ink);
    font-weight: 800;
  }
  .brand__dot { border-radius: 50%; background: var(--ink); flex: none; }
  .card--front .brand { left: 0; right: 0; top: 240px; top: 150px; justify-content: center; gap: 18px; font-size: 62px; }
  .card--front .brand__dot { width: 74px; height: 74px; }
  .card--back .brand { left: 42px; top: 56px; gap: 12px; font-size: 40px; }
  .card--back .brand__dot { width: 54px; height: 54px; }

  /* Front taglines */
  .front-lines {
    position: absolute;
    left: 0; right: 0; top: 306px;
    text-align: center;
    font-size: 17px;
    font-weight: 500;
    letter-spacing: 0.6px;
    line-height: 22px;
    color: var(--white);
  }
  .front-lines .services { color: var(--gold); }

  /* Back: owner */
  .owner {
    position: absolute;
    right: 42px; top: 51px;
    text-align: right;
  }
  .owner__name { font-size: 26px; font-weight: 500; line-height: 32px; }
  .owner__first { color: var(--brand-red); font-weight: 600; }
  .owner__role { font-size: 16px; line-height: 20px; }
  .owner__role b { color: var(--brand-red); font-weight: 600; }
  .owner__address {
    margin-top: 9px;
    font-size: 17px; line-height: 25px;
    color: var(--brand-red);
    letter-spacing: 0.3px;
  }

  /* Back: contact */
  .contact {
    position: absolute;
    left: 41px; top: 209px;
    list-style: none;
  }
  .contact li {
    display: flex; align-items: center; gap: 14px;
    height: 26px; margin-bottom: 6px;
    font-size: 17px; letter-spacing: 0.4px;
  }
  .contact svg { width: 27px; height: 27px; flex: none; }

  .feedback {
    position: absolute;
    left: 41px; top: 309px;
    font-size: 16px; line-height: 21px; letter-spacing: 0.3px;
  }
  .feedback span { color: var(--brand-red); }

  .listings {
    position: absolute;
    right: 42px; top: 305px;
    display: flex; align-items: center; gap: 12px;
  }
  .listing-badge { background: var(--badge-grey); border-radius: 14px; height: 28px; }
  .listing-badge--a { width: 104px; }
  .listing-badge--b { width: 152px; }
  .listing-badge--c { width: 70px; height: 48px; border-radius: 4px; background: var(--brand-red); }
</style>
</head>
<body>

<section class="card card--front" aria-label="Card front">
  <div class="brand"><span class="brand__dot"></span>Brolvane</div>
  <div class="front-lines">
    <p class="services">REPAIR | IMPROVE | MAINTAIN | REMODEL</p>
    <p>Commercial &amp; Residential Contractor</p>
    <p>Handyman, Technician</p>
  </div>
</section>

<section class="card card--back" aria-label="Card back">
  <div class="brand"><span class="brand__dot"></span>Brolvane</div>

  <div class="owner">
    <p class="owner__name"><span class="owner__first">Teodoro</span> Marques</p>
    <p class="owner__role">Owner of <b>Brolvane</b></p>
    <p class="owner__address">118/4 Larkin St, Harwood<br>NSW 2071, NY</p>
  </div>

  <ul class="contact">
    <li>
      <svg viewBox="0 0 24 24" aria-hidden="true"><circle cx="12" cy="12" r="12" fill="#e8232a"/><path d="M8.6 6.5l1.7 2.3c.3.4.2.9-.1 1.2l-.9.8c.6 1.3 1.6 2.4 2.9 3l.8-.9c.3-.3.8-.4 1.2-.1l2.3 1.6c.4.3.5.8.2 1.2l-.8 1c-.5.6-1.3.8-2 .6-3.3-1.1-5.9-3.7-7-7-.2-.7 0-1.5.6-2l1-.8c.4-.3.9-.2 1.1.1z" fill="#fff"/></svg>
      (215) 555 0148
    </li>
    <li>
      <svg viewBox="0 0 24 24" aria-hidden="true"><circle cx="12" cy="12" r="12" fill="#e8232a"/><rect x="6.5" y="8" width="11" height="8" rx="1" fill="#fff"/><path d="M6.8 8.4l5.2 4 5.2-4" fill="none" stroke="#e8232a" stroke-width="1.3"/></svg>
      brolvanehandymannyc@mailbox.com
    </li>
  </ul>

  <p class="feedback">We Are A 5 Star Company.<br>We Welcome Your <span>Feedback!</span></p>

  <div class="listings" aria-label="Listing badges">
    <span class="listing-badge listing-badge--a"></span>
    <span class="listing-badge listing-badge--b"></span>
    <span class="listing-badge listing-badge--c"></span>
  </div>
</section>

</body>
</html>
```